Letterhead & Business Card Design Project

Use existing logo to create a new letterhead and business card design. Looking for something clean modern using color options of black, white and gray. The green from the logo may be used lightly as an accent color.

Target Market(s)

Professional business people

Industry/Entity Type

Business

Requirements
Must have
• Business card with front and back design using existing logo.
Nice to have
• Professional presentation
Clean look
Should not have
• No oil rigs, pumpjacks or clip art.

```html
<!DOCTYPE html>
<html lang="en">
<head>
<meta charset="utf-8">
<title>Halvern Resources — Stationery</title>
<link href="https://fonts.googleapis.com/css2?family=Libre+Franklin:wght@400&display=swap" rel="stylesheet">
<style>
  :root {
    --paper: #ffffff;
    --ink: #111111;
    --band-black: #000000;
    --band-gray: #cfcfcf;
    --accent: #3ec43e;
    --text-light: #e6e6e6;
    --text-card: #d4d4d4;
    --watermark: #b5b5b5;
    --shadow: rgba(0,0,0,0.45);
  }
  * { margin: 0; padding: 0; box-sizing: border-box; }
  html, body { width: 1200px; height: 1000px; overflow: hidden; background: var(--paper); }
  body { position: relative; font-family: "Libre Franklin", Arial, sans-serif; }

  .letterhead {
    position: absolute; left: 155px; top: 75px; width: 615px; height: 838px;
    background: var(--paper); overflow: hidden;
    box-shadow: 2px 2px 8px var(--shadow);
  }
  .brand-name {
    color: var(--ink); font-weight: 400; text-transform: uppercase; line-height: 1;
  }
  .brand-name .primary { display: block; font-size: 46px; letter-spacing: 5px; }
  .brand-name .secondary { display: block; font-size: 18px; letter-spacing: 8px; margin-top: 10px; padding-left: 14px; }
  .letterhead .brand-name { position: absolute; left: 18px; top: 22px; }

  .letterhead .watermark {
    position: absolute; left: 175px; top: 282px;
    font-size: 150px; letter-spacing: 12px; color: var(--watermark);
    font-weight: 400; text-transform: uppercase; white-space: nowrap; line-height: 1;
    opacity: 0.85;
  }
  .letterhead .gray-band { position: absolute; left: 0; right: 0; top: 772px; height: 15px; background: var(--band-gray); }
  .letterhead .footer {
    position: absolute; left: 0; right: 0; top: 787px; height: 51px;
    background: var(--band-black); color: var(--text-light);
    font-size: 14.5px; text-align: center; line-height: 24px; padding-top: 3px;
  }
  .key { color: var(--accent); }

  .business-card {
    position: absolute; left: 527px; top: 502px; width: 555px; height: 329px;
    background: var(--paper); box-shadow: 1px 1px 7px var(--shadow);
  }
  .business-card .brand-name { position: absolute; left: 30px; top: 32px; }
  .business-card .gray-band { position: absolute; left: 0; right: 0; top: 135px; height: 20px; background: var(--band-gray); }
  .business-card .info-band {
    position: absolute; left: 0; right: 0; top: 155px; height: 135px;
    background: var(--band-black); color: var(--text-card);
    font-size: 16px; line-height: 24.2px;
  }
  .business-card .address-block { position: absolute; left: 31px; top: 8px; }
  .business-card .person-block { position: absolute; left: 348px; top: 22px; font-size: 17px; line-height: 30px; }
</style>
</head>
<body>
  <section class="letterhead">
    <div class="brand-name"><span class="primary">Halvern</span><span class="secondary">resources</span></div>
    <div class="watermark" aria-hidden="true">Halvern</div>
    <div class="gray-band"></div>
    <div class="footer">
      <div><span class="key">P</span> 316.555.0142 <span class="key">F</span> 316.555.0143 &nbsp;| <span class="key">W</span> www.halvernresources.com</div>
      <div><span class="key">A</span> 4520 North Birch Ave Suite 210 Wichita, Kansas 67205</div>
    </div>
  </section>

  <section class="business-card">
    <div class="brand-name"><span class="primary">Halvern</span><span class="secondary">resources</span></div>
    <div class="gray-band"></div>
    <div class="info-band">
      <div class="address-block">
        <div><span class="key">A</span> 4520 North Birch Ave Suite 210</div>
        <div>Wichita, Kansas 67205</div>
        <div><span class="key">P</span> 316.555.0142</div>
        <div><span class="key">F</span> 316.555.0143</div>
        <div><span class="key">W</span> www.halvernresources.com</div>
      </div>
      <div class="person-block">
        <div>Daniel R Hale</div>
        <div>Managing Member</div>
        <div><span class="key">C</span> 316.555.0199</div>
      </div>
    </div>
  </section>
</body>
</html>
```